Company profile urgent

Hi, I had my designer fail to deliver and I am looking for urgent designers job. Needs to go to print tomorrow the latest. I need company profile designed and finished, I do have a start of the project but did not like the overall design as it was too simple and not something I would asking for. This needs to be a great job and we are willing to pay for the right job.

This is pretty much a folded brochure as you will see from the document that is attached. On the front side do not remove LOGO from the actual position as it must stay there for the purposes of the cover that is going over and it has a whole for the logo where it is. Also, the pages are set as it should be so do not change the order of the pages, only the design, feel and look. This is for a travel company needs to look expensive, upscale, vip and must have clean design.

Needs to be done:

.

Needs to be done:

1) Get the design more attractive and modern. Not looking for cheap but high quality material.
2) As you can see we are tryin to present 4 products in the brochure that we do and this will be a folded brochure.
3) Infographics, especially the table ''when to travel'' needs updates and more style
4) This design is very steril, we are looking for clean and modern design
5) On the front page add Company profile text somewhere and add any design on home page is welcome BUT logo must stay where is
6) Please send final print ready documents as well as editable so we can move the logo if needed as it must fit the whole on a brochure holder
7) Last page with contacts very poorly done by my designer, needs upgrade with maybe infographics for phone, email web etc... ideas welcome
8) if you need more photos at the end is link to photo bank

Ideas welcome! Again we need it fast and clean.

Photo bank:
https://files.orvenbox.example/f/q7Lm2Xa9Tz4Pb8Kd

Designes that we linked: https://layoutmarket.example/item/company-profile-square-brochure/48817203?s_rank=8
https://layoutmarket.example/item/company-profile_square/51390628?s_rank=32
https://layoutmarket.example/item/square-brochure/53704916?s_rank=52

This is our webiste so you get the feeling of the colors: www.selvotrips.example

Important: Do not change text, or change pages, everything is as it should be just needs upgradede design! Logo on the first page must stay on the position as is.

Photo bank:

Target Market(s)

We are travel supplier targeting travel agents and travel companies

Industry/Entity Type

Travel Industry

Font styles to use
Serif
Sans Serif

Requirements
Must have
• https://files.orvenbox.example/f/w3Hn6Rc1Ys5Qe2Jv
Nice to have
• Cool design: https://layoutmarket.example/item/business-solution-brochure-template/46182057?s_rank=3
• Cool design 2: https://layoutmarket.example/item/travel-agency-catalog-brochure/47269815?s_rank=6
Should not have
• Do not change the dimensions. You have the design attached, indd file. Needs work and update.

```html
<!DOCTYPE html>
<html lang="en">
<head>
<meta charset="utf-8">
<title>Selvo Trips Croatia – Company Profile Spread</title>
<link href="https://fonts.googleapis.com/css2?family=Raleway:wght@300;400;600;700&display=swap" rel="stylesheet">
<style>
  :root{
    --red:#b3162c;
    --red-deep:#8c1426;
    --red-dark:#6f0f1e;
    --text:#4a4a4a;
    --paper:#ffffff;
    --mist:#ececec;
    --sea:#2f6f95;
    --stone:#b9a58a;
  }
  *{margin:0;padding:0;box-sizing:border-box}
  html,body{width:1200px;height:240px;overflow:hidden;background:var(--paper)}
  body{font-family:"Raleway",Arial,sans-serif;color:var(--text)}
  .spread{position:relative;width:1200px;height:240px;overflow:hidden;background:var(--paper)}
  .panel{position:absolute;top:0;height:240px;overflow:hidden}
  .photo{position:absolute;top:0;height:240px}
  .photo--coast{left:122px;width:236px;background:linear-gradient(160deg,#6d96b3 0%,#3f7599 35%,var(--sea) 55%,#8a7a5e 75%,#6f7a48 100%)}
  .photo--yacht{left:800px;width:280px;background:linear-gradient(200deg,#b9c9d6 0%,#7fa1b9 25%,#3b6d92 55%,#d9e3ea 80%,#2e5e83 100%)}
  .decor{position:absolute;top:0;left:0;width:1200px;height:240px;pointer-events:none}

  .tag{position:absolute;left:0;top:8px;background:var(--red);color:#fff;padding:4px 7px 4px 9px}
  .tag__title{font-weight:700;font-size:6.6px;letter-spacing:.3px;text-transform:uppercase}
  .tag__sub{font-weight:300;font-size:5.8px;line-height:6.6px;text-transform:uppercase;margin-top:1px}

  .copy{position:absolute;font-size:4.4px;line-height:5.3px;font-weight:400}
  .list{list-style:none;margin-top:6px}
  .list li{position:relative;padding-left:6px;margin-bottom:1.6px}
  .list li::before{content:"";position:absolute;left:0;top:1.3px;width:0;height:0;border-left:3px solid var(--red);border-top:1.5px solid transparent;border-bottom:1.5px solid transparent}

  .about{left:480px;width:240px;background:var(--red-deep);color:#fff}
  .about__title{position:absolute;left:20px;top:30px;font-size:6.6px;font-weight:700;letter-spacing:.3px;text-transform:uppercase}
  .about__copy{left:20px;top:42px;width:200px;color:#f4dfe2}
  .about__copy p+p{margin-top:5px}
  .values{position:absolute;left:10px;top:160px;width:220px;display:flex;justify-content:space-between}
  .value{width:52px;text-align:center}
  .value__icon{height:22px;display:flex;align-items:center;justify-content:center}
  .value__name{font-size:4.6px;font-weight:700;margin-top:4px;text-transform:uppercase}
  .value__text{font-size:3.9px;line-height:4.6px;font-weight:600;margin-top:2px}
</style>
</head>
<body>
<main class="spread">

  <!-- Customized trips -->
  <section class="panel" style="left:0;width:122px">
    <div class="tag" style="width:122px">
      <div class="tag__title">Customized Trips</div>
      <div class="tag__sub">Throughout Croatia<br>and Eastern Europe</div>
    </div>
    <div class="copy" style="left:9px;top:45px;width:106px">
      <p>We create exceptional, customized itineraries via our front line team of local experts, many of whom call Croatia home and are wonderfully experienced in the destinations Selvo Trips sells. Our sales representatives are consistently living the destinations, and receive constant education to ensure they are up to date on product news, trends and discoveries which will ensure you have the best information at your fingertips to recommend to your clients.</p>
      <ul class="list">
        <li>Itineraries crafted to perfection according to your client's interests and preferences</li>
        <li>Fast turnaround and guaranteed 48H delivery</li>
        <li>Unlimited revisions at no cost</li>
        <li>Wide selection of handpicked high-end accommodations including hotels and private villas</li>
        <li>Only selling tours that our team has experienced personally</li>
        <li>Licensed and in-house trained guides for all excursions and transfers</li>
        <li>Private transfers and chauffeur service available in a variety of vehicles</li>
        <li>Combined luxury land and boating itineraries</li>
        <li>Shore trips: Our team customizes private daily trips for your cruise clients visiting Croatia, Slovenia, and Montenegro</li>
      </ul>
    </div>
  </section>

  <div class="photo photo--coast" role="img" aria-label="Aerial view of a walled old town on the Adriatic coast with a winding coastal road"></div>

  <!-- Small group trips -->
  <section class="panel" style="left:358px;width:122px">
    <div class="tag" style="width:122px">
      <div class="tag__title">Small Group Trips</div>
      <div class="tag__sub">To Croatia<br>and Eastern Europe</div>
    </div>
    <div class="copy" style="left:9px;top:45px;width:106px">
      <p>Work with our team of local destination group experts to develop the finest programs for 10 pax or more. Our group specialists have all the experience to be able to work with you and create perfectly balanced itineraries and agendas to meet your group's pace, activity level and interests.</p>
      <ul class="list">
        <li>Exclusive group itineraries designed to meet the way your group travels</li>
        <li>Special booking conditions for added values, and 1 traveler free on every 15th traveler</li>
        <li>Group rates available</li>
        <li>Use of only high class coaches</li>
        <li>Combination of land and sea options available</li>
      </ul>
    </div>
  </section>

  <!-- About -->
  <section class="panel about">
    <svg class="decor" style="left:0;width:240px" viewBox="0 0 240 240" aria-hidden="true">
      <polygon points="0,0 60,0 0,70" fill="#9c1a2d"/>
      <polygon points="240,0 170,0 240,90" fill="#7d1122"/>
      <polygon points="0,240 120,150 240,240" fill="#7a1021"/>
      <polygon points="120,150 240,60 240,240" fill="#841325" opacity=".7"/>
    </svg>
    <h2 class="about__title">About Selvo Trips Croatia</h2>
    <div class="copy about__copy">
      <p>Since 2003, our team is working specifically on crafting the tours to show all the unique experiences in Croatia and beyond including Montenegro, Serbia, Bosnia and Herzegovina, Greece, and Albania. Selvo Trips Croatia is fully family owned and what we offer goes well beyond a travel package, we want all travelers to feel like part of our family. The company is focused on detailed personalized services for travelers that are demanding the ultimate level of service, using carefully hand-selected partners, drivers and guides on each destination to ensure the optimal travel experience.</p>
      <p>Our mission is to always offer exclusive experiences out of the public eyes that are preserved for the most discerning travelers to discover the authentic way of life in Croatia and Eastern Europe. We feel that testing and staying on top of the new travel trends on the destinations, offering only extraordinary pre-checked activities is our obligation and it is something we do on a daily basis. If you are looking to have a partner that will help you provide experiences that can't be found online, we are the right partner for you as our goal is to be your strongest local link you can always count on.</p>
    </div>
    <div class="values">
      <div class="value">
        <div class="value__icon">
          <svg width="18" height="21" viewBox="0 0 18 21" aria-hidden="true"><path d="M9 1 L17 4 V10 C17 15 13 18.5 9 20 C5 18.5 1 15 1 10 V4 Z" fill="#fff"/><path d="M5 10.5 L8 13.5 L13 7.5" fill="none" stroke="var(--red-deep)" stroke-width="1.8"/></svg>
        </div>
        <div class="value__name">Reliability</div>
        <div class="value__text">Over 13 years of experience with over 100 thousand happily served travelers.</div>
      </div>
      <div class="value">
        <div class="value__icon">
          <div role="img" aria-label="Outline map of Croatia" style="width:22px;height:18px;background:#f3e3e6;border-radius:2px"></div>
        </div>
        <div class="value__name">Local Experiences</div>
        <div class="value__text">Local know-how that guarantees extraordinary local experience.</div>
      </div>
      <div class="value">
        <div class="value__icon">
          <svg width="22" height="18" viewBox="0 0 22 18" aria-hidden="true"><rect width="22" height="18" rx="3" fill="#fff"/><text x="11" y="12.5" text-anchor="middle" font-family="Raleway,sans-serif" font-weight="700" font-size="9" fill="var(--red-deep)">VIP</text></svg>
        </div>
        <div class="value__name">Xclusivity</div>
        <div class="value__text">Access to activities and spots that are out of the public eye for most selective clients.</div>
      </div>
      <div class="value">
        <div class="value__icon">
          <div role="img" aria-label="Icon of a personal concierge greeting a traveler" style="width:20px;height:20px;background:#f3e3e6;border-radius:50%"></div>
        </div>
        <div class="value__name">Personal Approach</div>
        <div class="value__text">Local concierge and host is assigned to every client traveling with us who is at your client's full disposal.</div>
      </div>
    </div>
  </section>

  <div class="photo photo--yacht" role="img" aria-label="Luxury motor yacht speeding across the sea leaving a white wake"></div>

  <!-- Yachting -->
  <section class="panel" style="left:720px;width:122px;background:var(--paper)">
    <div class="tag" style="width:122px">
      <div class="tag__title">Yachting</div>
    </div>
    <div class="copy" style="left:9px;top:52px;width:100px">
      <p>Our yachting department has extensive knowledge of the Adriatic coast and all the destinations on the sea to create the optimal customized routes. Choose between 200,000 vessels in Croatia, available for private explorations of the Adriatic coast and Croatia's 1200 + islands.</p>
      <ul class="list">
        <li>Pre-checked skippers and crew</li>
        <li>Customized routes</li>
        <li>Sailboats</li>
        <li>Catamarans</li>
        <li>Gullets</li>
        <li>Motor Yachts</li>
        <li>Mega Yachts</li>
      </ul>
    </div>
  </section>

  <!-- Gourmet -->
  <section class="panel" style="left:1080px;width:120px">
    <div class="tag" style="width:120px">
      <div class="tag__title">Tastoria</div>
      <div class="tag__sub">The Art of<br>Croatian Gourmet</div>
    </div>
    <div class="copy" style="left:8px;top:45px;width:106px">
      <p>What does it mean to be Tastoria? It takes a blend of adventurous minds, a dash of creativity and an insider's scoop to the ultimate local gourmet experiences and fortunately this secret society exists. Launched in 2015, this special department of our company deals with testing and trying local wineries, farms, and restaurants to be able to suggest and provide outstanding gourmet daily activities in Croatia. As of now, we included about 20 boutique, family owned wineries and local farms across Croatia that offer incredibly delicious experiences that have no equal. It is always the best to immerse and experience the local culture through its food and wine.</p>
      <ul class="list">
        <li>Cooking classes and preparation of local dishes with locally recognized chefs</li>
        <li>Grape harvests and participating in making award winning wines</li>
        <li>Olive oil preparation and harvesting</li>
        <li>Truffle hunting</li>
      </ul>
    </div>
  </section>

  <!-- Facet overlays -->
  <svg class="decor" viewBox="0 0 1200 240" aria-hidden="true">
    <polygon points="122,0 165,0 122,35" fill="#fff" opacity=".55"/>
    <polygon points="358,140 358,240 300,240" fill="#fff" opacity=".35"/>
    <polygon points="358,0 420,0 358,60" fill="#e9e9e9" opacity=".6"/>
    <polygon points="480,0 480,240 440,240" fill="var(--red)" opacity=".15"/>
    <polygon points="800,0 842,0 842,240 800,240" fill="#fff"/>
    <polygon points="842,0 900,0 842,120" fill="#fff" opacity=".8"/>
    <polygon points="842,120 842,240 900,240" fill="#fff" opacity=".6"/>
    <polygon points="1080,0 1040,0 1080,60" fill="#fff" opacity=".45"/>
    <polygon points="1080,200 1080,240 1040,240" fill="var(--red)" opacity=".5"/>
  </svg>
</main>
</body>
</html>
```